Change logo on company documents

I want to change the logo on all company documents and change them company name that is written in certain places in the text.

Target Market(s)

Construction/Residential Home Remodeling

Colors

Designer to choose colors to be used in the design.

```html
<!DOCTYPE html>
<html lang="en">
<head>
<meta charset="utf-8">
<title>Proposal – Payment Schedule</title>
<link href="https://fonts.googleapis.com/css2?family=Arimo:wght@400;700&family=Carlito:ital,wght@0,400;0,700;1,700&display=swap" rel="stylesheet">
<style>
  :root {
    --ink: #000000;
    --ink-soft: #222222;
    --muted: #7a7a7a;
    --header-fill: #f1f1f1;
    --page: #ffffff;
    --frame: #555555;
  }
  * { box-sizing: border-box; margin: 0; padding: 0; }
  html, body { width: 910px; height: 1200px; overflow: hidden; background: var(--page); }
  .sheet {
    position: relative;
    width: 910px; height: 1200px;
    border: 1px solid var(--frame);
    color: var(--ink);
    font-family: "Arimo", Arial, sans-serif;
  }
  .brand {
    position: absolute; left: 58px; top: 88px;
    display: flex; align-items: center; gap: 10px;
    font-family: "Carlito", Calibri, sans-serif;
    font-weight: 700; font-size: 19px; line-height: 21px;
    letter-spacing: 0.5px; color: var(--ink);
  }
  .brand-dot { width: 22px; height: 22px; border-radius: 50%; background: var(--ink); flex: none; }
  .contact {
    position: absolute; right: 71px; top: 45px;
    text-align: right;
    font-family: "Carlito", Calibri, sans-serif;
    font-size: 16px; line-height: 21.5px; letter-spacing: 0.8px;
    color: var(--ink-soft);
  }
  .contact .label { margin-right: 6px; }
  .section-title {
    position: absolute; left: 35px;
    font-size: 17.5px; font-weight: 700;
  }
  .title-schedule { top: 205px; }
  .title-terms { top: 378px; }
  .schedule {
    position: absolute; left: 41px; top: 236px;
    width: 834px; border-collapse: collapse;
    font-size: 15px;
  }
  .schedule th, .schedule td {
    border: 1.3px solid var(--ink);
    height: 29px; padding: 0 10px;
    text-align: left; vertical-align: middle;
  }
  .schedule th { background: var(--header-fill); font-weight: 700; }
  .schedule .col-stage { width: 288px; }
  .schedule .col-amount { width: 273px; }
  .terms {
    position: absolute; left: 35px; top: 410px; width: 845px;
    font-size: 11.6px; line-height: 18px;
  }
  .signature {
    position: absolute; width: 347px;
    font-family: "Carlito", Calibri, sans-serif; font-size: 13.5px;
    color: var(--ink-soft);
  }
  .sig-homeowner { left: 67px; }
  .sig-contractor { left: 493px; }
  .sig-line { position: absolute; left: 0; width: 347px; border-top: 1.3px solid var(--ink); }
  .sig-name-line { top: 486px; }
  .sig-date-line { top: 528px; }
  .sig-label { position: absolute; left: 0; }
  .sig-name { top: 490px; }
  .sig-date { top: 561px; }
  .note {
    position: absolute; left: 0; right: 0; top: 598px;
    text-align: center;
    font-family: "Carlito", Calibri, sans-serif;
    font-weight: 700; font-style: italic; font-size: 15px;
    color: var(--muted);
  }
</style>
</head>
<body>
<div class="sheet">
  <div class="brand">
    <span class="brand-dot"></span>
    <span class="brand-name">R MARLOW<br>CONSTRUCTION</span>
  </div>

  <address class="contact" style="font-style:normal">
    TWO LAKESHORE PLAZA<br>
    SUITE 1400 #1187<br>
    KENNER, LA 70062<br>
    <span class="label">P:</span> 504.555.0142<br>
    <span class="label">F:</span> 504.555.0198
  </address>

  <h2 class="section-title title-schedule">PAYMENT SCHEDULE</h2>
  <table class="schedule">
    <thead>
      <tr><th class="col-stage">Stage</th><th class="col-amount">Amount</th><th>Due</th></tr>
    </thead>
    <tbody>
      <tr><td>Deposit</td><td></td><td>Upon Acceptance</td></tr>
      <tr><td>Progress Payment</td><td></td><td></td></tr>
      <tr><td>Final Payment</td><td></td><td>Upon Completion</td></tr>
    </tbody>
  </table>

  <h2 class="section-title title-terms">TERMS &amp; CONDITIONS</h2>
  <p class="terms">All material is guaranteed to be as specified. All work to be completed in a workmanlike manner according to standard practices. Any alteration or deviation involving extra costs will be executed only upon written order. Owner to carry all necessary insurances. Workmanship warranty: 90 days.</p>

  <div class="signature sig-homeowner">
    <div class="sig-line sig-name-line"></div>
    <div class="sig-label sig-name">Homeowner</div>
    <div class="sig-line sig-date-line"></div>
    <div class="sig-label sig-date">Date</div>
  </div>
  <div class="signature sig-contractor">
    <div class="sig-line sig-name-line"></div>
    <div class="sig-label sig-name">R Marlow Construction</div>
    <div class="sig-line sig-date-line"></div>
    <div class="sig-label sig-date">Date</div>
  </div>

  <p class="note">Note: This proposal may be withdrawn by us if not accepted within 30 days.</p>
</div>
</body>
</html>
```